Business cards for Norwegian software consultancy business

We are in need of business cards for our Norwegian consultancy company.
“Talvik Brensor AS” specializes in software development, architecture and agile methodology, providing mostly on-site services at customers.
The cards should reflect a certain level of business professionalism with an elegant touch, while paying tribute to our modern and technological heritage. Our logo should be featured, as well as room for basic information about the cardholder and legal information of the company (company name, address and VAT number).
We would like our cards to reflect that we are a modern consulting company. It should present a professional image that people will remember. The texture and color pallette should reflect our professionalism and reliability, so we prefer a light color pallette with colors such as gray, white, blue and black. The number of colors used should however not be overwhelming, with the text being distinct and readable.
We are open to untraditional layouts and playful designs as long as they communicate the intent stated above.
You could also take a look at our website http://www.brensor.no for input on our visual profile.
Our logo is attached in the form of vectors and rasterized PNG. Please comment if you would like the black-white and/or inverted versions as well.
Architecture
Company information:
Talvik Brensor AS
Lindeholtveien 7, 3142 Vestskogen
461 82 915
info@brensor.no
www.brensor.no
Employee information:
Full name
Title
Email
Phone

```html
<!DOCTYPE html>
<html lang="en">
<head>
<meta charset="utf-8">
<title>Talvik Brensor AS – Business Cards</title>
<link rel="stylesheet" href="https://fonts.googleapis.com/css2?family=Lato:wght@400;700;900&family=Lora:ital@1&display=swap">
<style>
  :root {
    --stage: #2a2a2c;
    --card-light: #f4f4f4;
    --card-light-edge: #e2e2e2;
    --card-dark: #3a3a3c;
    --card-dark-edge: #2e2e30;
    --blue: #4a8cc4;
    --ink: #3c3c3e;
    --ink-soft: #6a6a6c;
    --rule: #555558;
    --paper-text: #f2f2f2;
    --grey-text: #c9c9cb;
  }
  * { box-sizing: border-box; margin: 0; padding: 0; }
  html, body { width: 1200px; height: 873px; overflow: hidden; }
  body {
    background: var(--stage);
    font-family: "Lato", Arial, sans-serif;
    position: relative;
  }
  .card {
    position: absolute;
    width: 600px;
    height: 340px;
    border-radius: 22px;
    overflow: hidden;
  }

  /* Front card */
  .card-front {
    left: 70px; top: 70px;
    background: linear-gradient(135deg, #fbfbfb 0%, var(--card-light) 55%, var(--card-light-edge) 100%);
    color: var(--ink);
  }
  .brand {
    position: absolute;
    display: flex;
    align-items: center;
    gap: 12px;
    font-weight: 400;
    letter-spacing: 3px;
    text-transform: uppercase;
    white-space: nowrap;
  }
  .brand-square { display: block; background: var(--blue); }
  .card-front .brand {
    left: 44px; top: 160px;
    font-size: 26px;
    letter-spacing: 2px;
    color: var(--ink);
  }
  .card-front .brand-square { width: 16px; height: 16px; }

  .holder {
    position: absolute;
    right: 40px; top: 32px;
    width: 300px;
    text-align: right;
  }
  .holder-name { font-size: 19px; font-weight: 700; color: var(--blue); }
  .holder-title { font-size: 11px; color: var(--ink-soft); margin-top: 2px; }
  .holder-rule { height: 1.5px; background: var(--rule); margin: 10px 0; }
  .company-name { font-size: 13px; font-weight: 900; color: var(--ink); letter-spacing: .5px; }
  .company-address { font-size: 12px; color: var(--blue); margin-top: 3px; white-space: nowrap; }
  .company-vat { font-size: 10px; color: var(--ink-soft); margin-top: 4px; }

  .contact {
    position: absolute;
    left: 44px; bottom: 34px;
    width: 230px;
    border-top: 1.5px solid var(--rule);
    padding-top: 10px;
    list-style: none;
    font-size: 12px;
    color: var(--ink);
  }
  .contact li { display: flex; align-items: center; gap: 10px; height: 22px; }
  .contact svg { width: 14px; height: 14px; flex: none; }

  /* Back card */
  .card-back {
    left: 530px; top: 463px;
    background: linear-gradient(135deg, #434345 0%, var(--card-dark) 50%, var(--card-dark-edge) 100%);
    color: var(--paper-text);
  }
  .card-back .backdrop {
    position: absolute; inset: 0;
    background: linear-gradient(160deg, rgba(255,255,255,.04), rgba(0,0,0,.06));
  }
  .tagline-top {
    position: absolute;
    right: 60px; top: 92px;
    font-family: "Lora", Georgia, serif;
    font-style: italic;
    font-size: 14px;
    color: var(--grey-text);
  }
  .card-back .brand {
    right: 60px; top: 122px;
    font-size: 40px;
    color: var(--paper-text);
  }
  .card-back .brand-square { width: 24px; height: 24px; }
  .services {
    position: absolute;
    left: 0; right: 0; top: 220px;
    text-align: center;
    font-size: 17px;
    font-weight: 700;
    color: var(--paper-text);
  }
</style>
</head>
<body>

  <section class="card card-front" aria-label="Business card front">
    <div class="holder">
      <p class="holder-name">Jonas Veldhaug</p>
      <p class="holder-title">Owner / Founder</p>
      <div class="holder-rule"></div>
      <p class="company-name">TALVIK BRENSOR AS</p>
      <p class="company-address">Lindeholtveien 7, 3142 Vestskogen, Norway</p>
      <p class="company-vat">VAT 912 448 305</p>
    </div>

    <div class="brand"><span class="brand-square"></span>Talvik Brensor</div>

    <ul class="contact">
      <li>
        <svg viewBox="0 0 14 14" aria-hidden="true"><rect x="1.5" y="1.5" width="11" height="11" rx="1.5" fill="none" stroke="#4a8cc4" stroke-width="1.5"/></svg>
        +47 461 82 915
      </li>
      <li>
        <svg viewBox="0 0 14 14" aria-hidden="true"><rect x="1" y="2.5" width="12" height="9" fill="#4a8cc4"/><path d="M1 2.5 L7 8 L13 2.5" fill="none" stroke="#f4f4f4" stroke-width="1.2"/></svg>
        info@brensor.no
      </li>
      <li>
        <svg viewBox="0 0 14 14" aria-hidden="true"><path d="M6 8 L8 6 M5 6.5 L3 8.5 a2 2 0 0 0 2.8 2.8 L7.5 9.5 M9 7.5 L11 5.5 a2 2 0 0 0 -2.8 -2.8 L6.5 4.5" fill="none" stroke="#4a8cc4" stroke-width="1.5" stroke-linecap="round"/></svg>
        www.brensor.no
      </li>
    </ul>
  </section>

  <section class="card card-back" aria-label="Business card back">
    <div class="backdrop" role="img" aria-label="Faint repeating brand-mark pattern across the dark card"></div>
    <p class="tagline-top">Development &amp; IT Services</p>
    <div class="brand"><span class="brand-square"></span>Talvik Brensor</div>
    <p class="services">Software Development, Project Management &amp; IT Operations</p>
  </section>

</body>
</html>
```